ruCover Business Card Design Project

We need a business card design for ruCover. ruCover is an underwriting agency. Underwriting agencies act on behalf of insurers, to underwrite insurance. We will be operating in specialised classes of insurance initially and looking to expand from there. We would like to see designs that incorporate our logo colours as well as a contrasting stand out colour - also we'd like the logo itself to be embossed on the card.

Insurance

Requirements
Must have
• Logo on front
Nice to have
• Logo solely featured on back of card
Should not have
• Please do not use comic cans font :)

```html
<!DOCTYPE html>
<html lang="en">
<head>
<meta charset="UTF-8">
<title>ruCover Business Cards</title>
<link rel="stylesheet" href="https://fonts.googleapis.com/css2?family=Arimo:wght@400;700&display=swap">
<style>
  :root {
    --backdrop: #e4e4e4;
    --card: #ffffff;
    --brand-blue: #1f4fa8;
    --brand-blue-dark: #173d85;
    --ink: #222222;
    --ink-soft: #4a4a4a;
    --on-blue: #ffffff;
  }
  * { box-sizing: border-box; margin: 0; padding: 0; }
  html, body {
    width: 1200px;
    height: 896px;
    overflow: hidden;
    background: var(--backdrop);
    font-family: "Arimo", Arial, sans-serif;
  }
  .stage { position: relative; width: 1200px; height: 896px; }
  .card {
    position: absolute;
    width: 540px;
    height: 309px;
    background: var(--card);
    box-shadow: 0 6px 18px rgba(0,0,0,0.18);
    overflow: hidden;
  }
  .card--front { left: 90px; top: 110px; }
  .card--back { left: 570px; top: 480px; }

  .card__band { position: absolute; left: 0; top: 0; width: 540px; height: 309px; }

  .brand-name {
    position: absolute;
    font-weight: 700;
    color: var(--ink);
    letter-spacing: 0;
    line-height: 1;
  }
  .card--front .brand-name { left: 34px; top: 66px; font-size: 36px; }
  .card--back .brand-name { right: 34px; top: 172px; font-size: 28px; }

  .person { position: absolute; right: 34px; top: 90px; text-align: right; }
  .person__name { font-size: 20px; color: var(--ink); letter-spacing: 0.5px; line-height: 1.2; }
  .person__role { font-size: 12px; color: var(--brand-blue); letter-spacing: 1.5px; margin-top: 3px; }

  .phones {
    position: absolute;
    left: 46px;
    top: 128px;
    font-size: 14px;
    color: var(--ink-soft);
    line-height: 1.5;
  }
  .phones__label { color: var(--brand-blue); font-weight: 700; margin-right: 5px; }

  .address {
    position: absolute;
    left: 34px;
    top: 236px;
    font-size: 12px;
    font-style: normal;
    color: var(--on-blue);
    letter-spacing: 1px;
    line-height: 1.5;
    text-transform: uppercase;
  }
  .website {
    position: absolute;
    right: 34px;
    top: 198px;
    font-size: 14px;
    color: var(--on-blue);
    letter-spacing: 1px;
  }
</style>
</head>
<body>
<main class="stage">

  <section class="card card--front" aria-label="Business card front">
    <svg class="card__band" viewBox="0 0 540 309" aria-hidden="true">
      <path d="M0,190 Q300,204 540,172 L540,309 L0,309 Z" fill="var(--brand-blue)"/>
      <path d="M0,184 Q300,198 540,166 L540,172 Q300,204 0,190 Z" fill="var(--brand-blue-dark)"/>
    </svg>

    <p class="brand-name">ruCover</p>

    <div class="person">
      <p class="person__name">JORDAN A. MERCER</p>
      <p class="person__role">OWNER</p>
    </div>

    <div class="phones">
      <p><span class="phones__label">T</span>555.210.7788</p>
      <p><span class="phones__label">F</span>555.210.7789</p>
    </div>

    <p class="website">rucoveragency.net</p>

    <address class="address">
      118 Harbour Road East<br>
      Kelvin Bay, KB 20417
    </address>
  </section>

  <section class="card card--back" aria-label="Business card back">
    <svg class="card__band" viewBox="0 0 540 309" aria-hidden="true">
      <path d="M0,264 Q270,276 540,246 L540,309 L0,309 Z" fill="var(--brand-blue)"/>
      <path d="M0,258 Q270,270 540,240 L540,246 Q270,276 0,264 Z" fill="var(--brand-blue-dark)"/>
    </svg>

    <p class="brand-name">ruCover</p>
  </section>

</main>
</body>
</html>
```